Corporate Identity Design for Travel Company

We need a brand book, that should include the following artwork:

Business card
Letterhead
Envelope (DL, C4, C5)
A4 folder
A4 paper for notes
E-mail signature
Power point template
Pen design

Please, submit your designs that include business card, letterhead and envelope. Once selected the winner, he will be asked to complete the project by creating the rest of the artwork.

Logo and project requirements are attached.

```html
<!DOCTYPE html>
<html lang="en">
<head>
<meta charset="utf-8">
<title>Tidewater Trails – Stationery</title>
<link href="https://fonts.googleapis.com/css2?family=Open+Sans:wght@300;400;600&display=swap" rel="stylesheet">
<style>
  :root {
    --bg: #e9e9ea;
    --paper: #fbfbfb;
    --ink: #3a3a3a;
    --ink-soft: #6b6b6b;
    --green: #5cb85a;
    --lime: #b6d140;
    --orange: #f0a33a;
    --sky: #96cfe0;
    --brand: #4a4d50;
  }
  * { margin: 0; padding: 0; box-sizing: border-box; }
  html, body { width: 800px; height: 1200px; overflow: hidden; }
  body {
    background: var(--bg);
    font-family: "Open Sans", Arial, sans-serif;
    color: var(--ink);
    position: relative;
  }
  .sheet { position: absolute; background: var(--paper); box-shadow: 0 1px 3px rgba(0,0,0,.12); }

  .color-bar { position: absolute; left: 0; right: 0; display: flex; }
  .color-bar span { height: 100%; }
  .c-green { background: var(--green); }
  .c-lime { background: var(--lime); }
  .c-orange { background: var(--orange); }
  .c-sky { background: var(--sky); }

  .brand { position: absolute; display: flex; align-items: center; gap: 8px; }
  .brand-mark { width: 14px; height: 14px; background: var(--green); border-radius: 3px; }
  .brand-name { font-weight: 300; color: var(--brand); line-height: 1.05; letter-spacing: .5px; }

  .contact { position: absolute; text-align: right; font-size: 6px; color: var(--ink-soft); line-height: 10px; }
  .contact b { font-weight: 400; color: var(--ink); }

  /* letterhead */
  .letterhead { left: 57px; top: 104px; width: 430px; height: 608px; }
  .letterhead .brand { left: 63px; top: 35px; }
  .letterhead .brand-name { font-size: 21px; }
  .letterhead .contact { right: 46px; top: 53px; }
  .letter-body { position: absolute; left: 61px; top: 160px; width: 324px; font-size: 6.6px; line-height: 12.6px; color: var(--ink); }
  .letter-body p { margin-bottom: 14px; }
  .signature { position: absolute; left: 61px; top: 472px; font-size: 6.8px; line-height: 13px; }
  .letter-date { position: absolute; right: 47px; top: 475px; font-size: 6.8px; }
  .letterhead .color-bar { bottom: 0; height: 6px; }

  /* business cards */
  .card { width: 184px; height: 104px; left: 542px; }
  .card .color-bar { height: 5px; }
  .card .bar-top { top: 0; }
  .card .bar-bottom { bottom: 0; }
  .card-front { top: 112px; }
  .card-front .brand { left: 33px; top: 32px; }
  .card-front .brand-name { font-size: 19px; }
  .card-back { top: 246px; }
  .card-name { position: absolute; left: 13px; top: 10px; font-size: 17px; font-weight: 400; color: var(--brand); letter-spacing: .4px; }
  .card-role { position: absolute; left: 13px; top: 34px; font-size: 6px; color: var(--ink-soft); letter-spacing: .3px; }
  .card-back .brand-mark { position: absolute; left: 24px; top: 55px; width: 26px; height: 26px; border-radius: 5px; }
  .card-back .contact { left: 78px; top: 50px; text-align: left; font-size: 4.8px; line-height: 8.8px; }

  /* envelope */
  .envelope { left: 59px; top: 770px; width: 447px; height: 217px; }
  .envelope .brand { left: 28px; top: 155px; }
  .envelope .brand-name { font-size: 19px; }
  .envelope .contact { right: 24px; top: 157px; line-height: 12.5px; }
  .envelope .color-bar { bottom: 0; height: 7px; }
</style>
</head>
<body>

<section class="sheet letterhead">
  <div class="brand">
    <span class="brand-mark"></span>
    <span class="brand-name">Tidewater<br>Trails</span>
  </div>
  <address class="contact">
    45 Harbor Lane - Coast Town, USA 54321<br>
    Tel: <b>+123 555 0142</b> &nbsp;|&nbsp; Fax: <b>+123 555 0143</b><br>
    www.tidewatertrails.com &nbsp;|&nbsp; marta@tidewatertrails.com
  </address>
  <div class="letter-body">
    <p>Dear Client,</p>
    <p style="margin-top:6px">Lorem ipsum dolor sit amet, consectetur adipiscing elit. Non igitur bene. Sed quot homines, tot sententiae; Hanc ergo intuens debet institutum illud quasi signum absolvere. Aliter enim explicari, quod quaeritur, non potest. Theophrastus mediocriterne delectat, cum tractat locos ab Aristotele ante tractatos? Hoc non est positum in nostra actione.</p>
    <p>Ergo infelix una molestia, fellx rursus, cum is ipse anulus in praecordiis piscis inventus est? Sed fortuna fortis; Cur tantas regiones barbarorum pedibus obiit, tot maria transmisit? Si verbum sequimur, primum longius verbum praepositum quam bonum.</p>
    <p>Bonum negas esse divitias, praeposìtum esse dicis? Cui Tubuli nomen odio non est? Nummus in Croesi divitiis obscuratur, pars est tamen divitiarum. Nunc omni virtuti vitium contrario nomine opponitur. Quis Pullum Numitorium Fregellanum, proditorem, quamquam rei publicae nostrae profuit, non odit? Sin tantum modo ad indicia veteris memoriae cognoscenda, curiosorum. Quod quidem iam fit etiam in Academia. At coluit ipse amicitias.</p>
    <p>Quae quidem sapientes sequuntur duce natura tamquam videntes; Quae diligentissime contra Aristonem dicuntur a Chryippo. Tamen a proposito, inquam, aberramus. Cur ipse Pythagoras et Aegyptum lustravit et Persarum magos adiit? Itaque primos congressus copulationesque et consuetudinum instituendarut.</p>
    <p>Yours Sincerely,</p>
  </div>
  <div class="signature">Marta Ozola<br>General Manager</div>
  <div class="letter-date">16.05.2013</div>
  <div class="color-bar"><span class="c-green" style="width:43.5%"></span><span class="c-lime" style="width:36%"></span><span class="c-orange" style="width:14.7%"></span><span class="c-sky" style="width:5.8%"></span></div>
</section>

<section class="sheet card card-front">
  <div class="color-bar bar-top"><span class="c-sky" style="width:20%"></span><span class="c-orange" style="width:25%"></span><span class="c-green" style="width:35%"></span><span class="c-lime" style="width:20%"></span></div>
  <div class="brand">
    <span class="brand-mark"></span>
    <span class="brand-name">Tidewater<br>Trails</span>
  </div>
  <div class="color-bar bar-bottom"><span class="c-green" style="width:52%"></span><span class="c-lime" style="width:28%"></span><span class="c-orange" style="width:14%"></span><span class="c-sky" style="width:6%"></span></div>
</section>

<section class="sheet card card-back">
  <h1 class="card-name">MARTA OZOLA</h1>
  <p class="card-role">GENERAL MANAGER</p>
  <span class="brand-mark"></span>
  <address class="contact">
    45 Harbor Lane - Coast Town, USA 54321<br>
    Tel: <b>+123 555 0142</b><br>
    Fax: <b>+123 555 0143</b><br>
    www.tidewatertrails.com<br>
    marta@tidewatertrails.com
  </address>
  <div class="color-bar bar-bottom"><span class="c-green" style="width:52%"></span><span class="c-lime" style="width:28%"></span><span class="c-orange" style="width:14%"></span><span class="c-sky" style="width:6%"></span></div>
</section>

<section class="sheet envelope">
  <div class="brand">
    <span class="brand-mark"></span>
    <span class="brand-name">Tidewater<br>Trails</span>
  </div>
  <address class="contact">
    45 Harbor Lane - Coast Town, USA 54321<br>
    Tel: <b>+123 555 0142</b> &nbsp;|&nbsp; Fax: <b>+123 555 0143</b><br>
    www.tidewatertrails.com &nbsp;|&nbsp; marta@tidewatertrails.com
  </address>
  <div class="color-bar"><span class="c-green" style="width:57%"></span><span class="c-lime" style="width:21%"></span><span class="c-orange" style="width:14%"></span><span class="c-sky" style="width:8%"></span></div>
</section>

</body>
</html>
```